One label design for 3 different sizes of honey bottles

Our honey company -- Amber Hollow Apiary -- needs new product labels, integrating our new name and logo. We would like one label design that presents equally well on three different sizes of plastic honey bottles. Designs should include a front and back label.

Keep in mind that we really like our old label. Please submit designs that have a similar color and font scheme as the old label.

In the uploaded files, you will find (1) detailed content instructions for each size label (2 lb, 1 lb, 8 oz), (2) photo of three plastic bottles without labels, (3) *.ai file for the new company logo, and (4) image of old package label.

Requirements
Must have
• Same look and feel as our old label, but with our new name and logo

```html
<!DOCTYPE html>
<html lang="en">
<head>
<meta charset="utf-8">
<title>Amber Hollow Apiary – Honey Labels</title>
<link rel="stylesheet" href="https://fonts.googleapis.com/css2?family=Abril+Fatface&family=Arvo:wght@700&family=Lato:wght@300;400;700&display=swap">
<style>
  :root {
    --backdrop: #8b5a2f;
    --cream: #f8f2e2;
    --ink: #3b3935;
    --tan: #e9d7b7;
    --ornament: #d9c7a6;
    --table: #ffffff;
    --note: #f6eadb;
  }
  html, body { margin: 0; padding: 0; width: 1200px; height: 1200px; overflow: hidden; background: var(--backdrop); }
  .sheet { display: block; width: 1200px; height: 1200px; }
  .sans { font-family: "Lato", sans-serif; font-weight: 300; fill: var(--ink); }
  .sans-bold { font-family: "Lato", sans-serif; font-weight: 700; fill: var(--ink); }
  .brand { font-family: "Lato", sans-serif; font-weight: 700; fill: var(--ink); }
  .tagline { font-family: "Lato", sans-serif; font-weight: 400; fill: var(--ink); word-spacing: 0.35em; }
  .display { font-family: "Abril Fatface", serif; fill: var(--ink); }
  .slab { font-family: "Arvo", serif; font-weight: 700; fill: var(--ink); letter-spacing: 0.06em; }
  .quote-mark { font-family: "Abril Fatface", serif; fill: var(--ink); }
  .mid { text-anchor: middle; }
  .end { text-anchor: end; }
  .note { font-family: "Lato", sans-serif; font-weight: 300; fill: var(--note); }
  .label-face { fill: url(#labelTone); }
  .outer-line { fill: none; stroke: var(--ink); stroke-width: 3; }
  .inner-line { fill: none; stroke: var(--ink); stroke-width: 1.5; }
  .rule { stroke: var(--ink); stroke-width: 2; }
  .rule-thin { stroke: var(--ink); stroke-width: 1.3; }
  .banner { fill: var(--cream); stroke: var(--ink); stroke-width: 2.5; }
  .quote-band { fill: var(--tan); }
  .fact-table { fill: var(--table); }
  .ornament { fill: var(--ornament); opacity: 0.7; }
  .illustration { fill: var(--tan); opacity: 0.45; }
  .brand-dot { fill: var(--ink); }
</style>
</head>
<body>
<svg class="sheet" viewBox="0 0 1932 1932" xmlns="http://www.w3.org/2000/svg">
  <defs>
    <radialGradient id="labelTone" cx="50%" cy="40%" r="75%">
      <stop offset="0" stop-color="#faf5e8"/>
      <stop offset="1" stop-color="#f3ead4"/>
    </radialGradient>
  </defs>

  <!-- ===== 2 LB FRONT ===== -->
  <g class="front-label front-2lb">
    <path class="label-face" d="M115,60 H620 L645,85 V1057 H90 V85 Z"/>
    <rect class="illustration" x="108" y="500" width="100" height="190" rx="40" role="img" aria-label="Faint bee illustration"/>
    <rect class="ornament" x="107" y="900" width="100" height="138" rx="28" role="img" aria-label="Scrollwork corner ornament"/>
    <rect class="ornament" x="528" y="900" width="100" height="138" rx="28" role="img" aria-label="Scrollwork corner ornament"/>
    <path class="outer-line" d="M115,60 H620 L645,85 V1057 H90 V85 Z"/>
    <path class="inner-line" d="M128,75 H607 L630,98 V1042 H105 V98 Z"/>
    <text class="tagline mid" x="367" y="186" font-size="40">LOCAL · PURE · RAW</text>
    <path class="banner" d="M55,265 H680 L700,285 V470 L680,490 H55 L35,470 V285 Z"/>
    <text class="display mid" x="367" y="450" font-size="190" textLength="590" lengthAdjust="spacingAndGlyphs">HONEY</text>
    <circle class="brand-dot" cx="367" cy="640" r="20"/>
    <text class="brand mid" x="367" y="725" font-size="48">Amber Hollow</text>
    <text class="brand mid" x="367" y="785" font-size="48">Apiary</text>
    <text class="sans mid" x="367" y="906" font-size="40">NET WEIGHT</text>
    <line class="rule" x1="218" y1="918" x2="518" y2="918"/>
    <text class="sans-bold mid" x="367" y="980" font-size="56">2 LB (907 g)</text>
  </g>

  <!-- ===== 2 LB BACK ===== -->
  <g class="back-label back-2lb">
    <rect class="label-face" x="741" y="60" width="664" height="997"/>
    <rect class="ornament" x="759" y="982" width="150" height="56" rx="22" role="img" aria-label="Scrollwork corner ornament"/>
    <rect class="ornament" x="1238" y="982" width="150" height="56" rx="22" role="img" aria-label="Scrollwork corner ornament"/>
    <rect class="outer-line" x="741" y="60" width="664" height="997"/>
    <path class="inner-line" d="M782,76 H1365 L1390,101 V1040 H757 V101 Z"/>
    <polygon class="quote-band" points="860,245 915,107 1240,107 1300,245 1240,382 915,382"/>
    <text class="quote-mark" x="918" y="175" font-size="90">“</text>
    <text class="quote-mark" x="1180" y="425" font-size="90">”</text>
    <text class="sans mid" x="1073" y="185" font-size="32" font-weight="400">AMBER HOLLOW APIARY</text>
    <text class="sans mid" x="1073" y="219" font-size="29">promises <tspan class="sans-bold">100%</tspan> pure honey,</text>
    <text class="sans mid" x="1073" y="253" font-size="29">never pasteurized, &amp; sourced exclusively</text>
    <text class="sans mid" x="1073" y="287" font-size="29">from beehives</text>
    <text class="sans mid" x="1073" y="322" font-size="29">we keep near Foxglove Springs,</text>
    <text class="sans mid" x="1073" y="356" font-size="29">West Virginia</text>
    <text class="slab mid" x="1073" y="440" font-size="34">NUTRITION FACTS</text>
    <rect class="fact-table" x="775" y="452" width="597" height="303"/>
    <text class="sans mid" x="935" y="483" font-size="28">SERVINGS: 43</text>
    <text class="sans mid" x="1215" y="481" font-size="24" font-weight="400">Serv. size: 1 Tbsp (21g)</text>
    <line class="rule" x1="790" y1="494" x2="1360" y2="494"/>
    <line class="rule" x1="1073" y1="494" x2="1073" y2="755"/>
    <text class="sans" font-size="24"><tspan x="787" y="520">Calories</tspan><tspan x="787" y="557">Total Fat</tspan><tspan x="787" y="594">Sat. Fat</tspan><tspan x="787" y="631">Trans Fat</tspan><tspan x="787" y="668">Cholest.</tspan><tspan x="787" y="705">Sodium</tspan><tspan x="787" y="742">Total Carb.</tspan></text>
    <text class="sans" font-size="24"><tspan x="920" y="520">60</tspan><tspan x="920" y="557">0g (0% DV)</tspan><tspan x="920" y="594">0g (0% DV)</tspan><tspan x="920" y="631">0g</tspan><tspan x="920" y="668">0mg (0% DV)</tspan><tspan x="920" y="705">0mg (0% DV)</tspan><tspan x="920" y="742">17g (6% DV)</tspan></text>
    <text class="sans" font-size="24"><tspan x="1098" y="520">Fiber</tspan><tspan x="1098" y="557">Total Sugars</tspan><tspan x="1098" y="594">Protein</tspan><tspan x="1098" y="631">Vit. D</tspan><tspan x="1098" y="668">Calcium</tspan><tspan x="1098" y="705">Iron</tspan><tspan x="1098" y="742">Potas.</tspan></text>
    <text class="sans" font-size="24"><tspan x="1232" y="520">0g (0% DV)</tspan><tspan x="1232" y="557">17g (34% DV)</tspan><tspan x="1232" y="594">0g</tspan><tspan x="1232" y="631">0g (0% DV)</tspan><tspan x="1232" y="668">0g (0% DV)</tspan><tspan x="1232" y="705">0g (0% DV)</tspan><tspan x="1232" y="742">0g (0% DV)</tspan></text>
    <text class="sans mid" x="1073" y="798" font-size="24">One serving adds 17g of sugar of your diet and</text>
    <text class="sans mid" x="1073" y="830" font-size="24">represents 34% of the Daily Value for Added Sugars.</text>
    <line class="rule" x1="775" y1="858" x2="1372" y2="858"/>
    <line class="rule" x1="965" y1="858" x2="965" y2="972"/>
    <text class="sans end" font-size="17" font-weight="400"><tspan x="955" y="888">“DO NOT FEED HONEY</tspan><tspan x="955" y="925">TO INFANTS UNDER</tspan><tspan x="955" y="962">ONE YEAR OLD”</tspan></text>
    <text class="sans" font-size="23" font-weight="400"><tspan x="977" y="890">Amber Hollow Apiary, 112 Quarry Lane</tspan><tspan x="977" y="927">Foxglove Springs, WV 25400</tspan><tspan x="977" y="964">www.amberhollowapiary.com</tspan></text>
  </g>

  <!-- ===== SIZE NOTES ===== -->
  <g class="size-notes">
    <text class="note" font-size="22"><tspan x="1480" y="323">2LB :  3 inches wide by 4.5 inches tall</tspan><tspan x="1480" y="352">1 LB : 2 inches wide by 3.5 inches talL</tspan><tspan x="1480" y="382">8 OZ : 1.75 inches wide by 2.5 inches tall</tspan><tspan x="1480" y="441">Please let me know if you need</tspan><tspan x="1480" y="470">any changes in the design.</tspan></text>
  </g>

  <!-- ===== 1 LB FRONT ===== -->
  <g class="front-label front-1lb">
    <path class="label-face" d="M102,1090 H427 L449,1112 V1865 H80 V1112 Z"/>
    <rect class="illustration" x="97" y="1395" width="75" height="135" rx="30" role="img" aria-label="Faint bee illustration"/>
    <rect class="ornament" x="96" y="1752" width="64" height="96" rx="20" role="img" aria-label="Scrollwork corner ornament"/>
    <rect class="ornament" x="370" y="1752" width="63" height="96" rx="20" role="img" aria-label="Scrollwork corner ornament"/>
    <path class="outer-line" d="M102,1090 H427 L449,1112 V1865 H80 V1112 Z"/>
    <path class="inner-line" d="M114,1105 H415 L434,1124 V1850 H95 V1124 Z"/>
    <text class="tagline mid" x="264" y="1173" font-size="28">LOCAL · PURE · RAW</text>
    <path class="banner" d="M58,1243 H471 L487,1259 V1376 L471,1392 H58 L42,1376 V1259 Z"/>
    <text class="display mid" x="264" y="1365" font-size="140" textLength="392" lengthAdjust="spacingAndGlyphs">HONEY</text>
    <circle class="brand-dot" cx="264" cy="1495" r="14"/>
    <text class="brand mid" x="264" y="1560" font-size="32">Amber Hollow</text>
    <text class="brand mid" x="264" y="1600" font-size="32">Apiary</text>
    <text class="sans mid" x="264" y="1740" font-size="27">NET WEIGHT</text>
    <line class="rule" x1="165" y1="1748" x2="365" y2="1748"/>
    <text class="sans-bold mid" x="264" y="1790" font-size="38">1 LB (454 g)</text>
  </g>

  <!-- ===== 1 LB BACK ===== -->
  <g class="back-label back-1lb">
    <rect class="label-face" x="522" y="1088" width="445" height="777"/>
    <rect class="ornament" x="536" y="1796" width="100" height="54" rx="18" role="img" aria-label="Scrollwork corner ornament"/>
    <rect class="ornament" x="852" y="1796" width="100" height="54" rx="18" role="img" aria-label="Scrollwork corner ornament"/>
    <path class="inner-line" d="M552,1100 H936 L955,1119 V1853 H533 V1119 Z"/>
    <polygon class="quote-band" points="570,1260 610,1170 880,1170 918,1260 880,1350 610,1350"/>
    <text class="quote-mark" x="626" y="1195" font-size="60">“</text>
    <text class="quote-mark" x="826" y="1378" font-size="60">”</text>
    <text class="sans mid" x="745" y="1202" font-size="23" font-weight="400">AMBER HOLLOW APIARY</text>
    <text class="sans mid" x="745" y="1229" font-size="20">promises <tspan class="sans-bold">100%</tspan> pure honey,</text>
    <text class="sans mid" x="745" y="1255" font-size="20">never pasteurized, &amp; sourced exclusively</text>
    <text class="sans mid" x="745" y="1281" font-size="20">from beehives</text>
    <text class="sans mid" x="745" y="1307" font-size="20">we keep near Foxglove Springs,</text>
    <text class="sans mid" x="745" y="1333" font-size="20">West Virginia</text>
    <text class="slab mid" x="745" y="1400" font-size="23">NUTRITION FACTS</text>
    <rect class="fact-table" x="545" y="1413" width="398" height="224"/>
    <text class="sans mid" x="652" y="1436" font-size="19">SERVINGS: 22</text>
    <text class="sans mid" x="838" y="1434" font-size="15" font-weight="400">Serv. size: 1 Tbsp (21g)</text>
    <line class="rule-thin" x1="548" y1="1442" x2="940" y2="1442"/>
    <line class="rule-thin" x1="745" y1="1442" x2="745" y2="1637"/>
    <text class="sans" font-size="16"><tspan x="553" y="1462">Calories</tspan><tspan x="553" y="1490">Total Fat</tspan><tspan x="553" y="1517">Sat. Fat</tspan><tspan x="553" y="1545">Trans Fat</tspan><tspan x="553" y="1573">Cholest.</tspan><tspan x="553" y="1600">Sodium</tspan><tspan x="553" y="1628">Total Carb.</tspan></text>
    <text class="sans" font-size="16"><tspan x="642" y="1462">60</tspan><tspan x="642" y="1490">0g (0% DV)</tspan><tspan x="642" y="1517">0g (0% DV)</tspan><tspan x="642" y="1545">0g</tspan><tspan x="642" y="1573">0mg (0% DV)</tspan><tspan x="642" y="1600">0mg (0% DV)</tspan><tspan x="642" y="1628">17g (6% DV)</tspan></text>
    <text class="sans" font-size="16"><tspan x="761" y="1462">Fiber</tspan><tspan x="761" y="1490">Total Sugars</tspan><tspan x="761" y="1517">Protein</tspan><tspan x="761" y="1545">Vit. D</tspan><tspan x="761" y="1573">Calcium</tspan><tspan x="761" y="1600">Iron</tspan><tspan x="761" y="1628">Potas.</tspan></text>
    <text class="sans" font-size="16"><tspan x="849" y="1462">0g (0% DV)</tspan><tspan x="849" y="1490">17g (34% DV)</tspan><tspan x="849" y="1517">0g</tspan><tspan x="849" y="1545">0g (0% DV)</tspan><tspan x="849" y="1573">0g (0% DV)</tspan><tspan x="849" y="1600">0g (0% DV)</tspan><tspan x="849" y="1628">0g (0% DV)</tspan></text>
    <text class="sans mid" x="745" y="1662" font-size="15">One serving adds 17g of sugar of your diet and</text>
    <text class="sans mid" x="745" y="1682" font-size="15">represents 34% of the Daily Value for Added Sugars.</text>
    <line class="rule-thin" x1="545" y1="1708" x2="943" y2="1708"/>
    <line class="rule-thin" x1="672" y1="1708" x2="672" y2="1785"/>
    <text class="sans end" font-size="11" font-weight="400"><tspan x="666" y="1728">“DO NOT FEED HONEY</tspan><tspan x="666" y="1753">TO INFANTS UNDER</tspan><tspan x="666" y="1777">ONE YEAR OLD”</tspan></text>
    <text class="sans" font-size="14.5" font-weight="400"><tspan x="680" y="1730">Amber Hollow Apiary, 112 Quarry Lane</tspan><tspan x="680" y="1754">Foxglove Springs, WV 25400</tspan><tspan x="680" y="1779">www.amberhollowapiary.com</tspan></text>
  </g>

  <!-- ===== 8 OZ FRONT ===== -->
  <g class="front-label front-8oz">
    <path class="label-face" d="M1083,1122 H1370 L1388,1140 V1675 H1065 V1140 Z"/>
    <rect class="illustration" x="1080" y="1360" width="70" height="110" rx="26" role="img" aria-label="Faint bee illustration"/>
    <rect class="ornament" x="1080" y="1590" width="52" height="70" rx="16" role="img" aria-label="Scrollwork corner ornament"/>
    <rect class="ornament" x="1322" y="1590" width="52" height="70" rx="16" role="img" aria-label="Scrollwork corner ornament"/>
    <path class="outer-line" d="M1083,1122 H1370 L1388,1140 V1675 H1065 V1140 Z"/>
    <path class="inner-line" d="M1094,1135 H1360 L1376,1151 V1662 H1078 V1151 Z"/>
    <text class="tagline mid" x="1226" y="1178" font-size="26">LOCAL · PURE · RAW</text>
    <path class="banner" d="M1046,1203 H1406 L1420,1217 V1319 L1406,1333 H1046 L1032,1319 V1217 Z"/>
    <text class="display mid" x="1226" y="1310" font-size="125" textLength="345" lengthAdjust="spacingAndGlyphs">HONEY</text>
    <circle class="brand-dot" cx="1226" cy="1400" r="12"/>
    <text class="brand mid" x="1226" y="1455" font-size="28">Amber Hollow</text>
    <text class="brand mid" x="1226" y="1490" font-size="28">Apiary</text>
    <text class="sans mid" x="1226" y="1578" font-size="24">NET WEIGHT</text>
    <line class="rule" x1="1138" y1="1585" x2="1315" y2="1585"/>
    <text class="sans-bold mid" x="1226" y="1621" font-size="34">8 oz (227 g)</text>
  </g>

  <!-- ===== 8 OZ BACK ===== -->
  <g class="back-label back-8oz">
    <rect class="label-face" x="1446" y="1122" width="386" height="553"/>
    <rect class="ornament" x="1458" y="1634" width="80" height="28" rx="12" role="img" aria-label="Scrollwork corner ornament"/>
    <rect class="ornament" x="1740" y="1634" width="80" height="28" rx="12" role="img" aria-label="Scrollwork corner ornament"/>
    <rect class="outer-line" x="1446" y="1122" width="386" height="553"/>
    <path class="inner-line" d="M1472,1132 H1806 L1822,1148 V1665 H1456 V1148 Z"/>
    <polygon class="quote-band" points="1515,1215 1550,1142 1745,1142 1778,1215 1745,1290 1550,1290"/>
    <text class="quote-mark" x="1555" y="1178" font-size="45">“</text>
    <text class="quote-mark" x="1697" y="1318" font-size="45">”</text>
    <text class="sans mid" x="1640" y="1184" font-size="18" font-weight="400">AMBER HOLLOW APIARY</text>
    <text class="sans mid" x="1640" y="1203" font-size="14">promises <tspan class="sans-bold">100%</tspan> pure honey,</text>
    <text class="sans mid" x="1640" y="1222" font-size="14">never pasteurized, &amp; sourced exclusively</text>
    <text class="sans mid" x="1640" y="1241" font-size="14">from beehives</text>
    <text class="sans mid" x="1640" y="1260" font-size="14">we keep near Foxglove Springs,</text>
    <text class="sans mid" x="1640" y="1279" font-size="14">West Virginia</text>
    <text class="slab mid" x="1640" y="1325" font-size="18">NUTRITION FACTS</text>
    <rect class="fact-table" x="1465" y="1333" width="353" height="179"/>
    <text class="sans mid" x="1558" y="1353" font-size="15">SERVINGS: 11</text>
    <text class="sans mid" x="1722" y="1351" font-size="12" font-weight="400">Serv. size: 1 Tbsp (21g)</text>
    <line class="rule-thin" x1="1467" y1="1358" x2="1815" y2="1358"/>
    <line class="rule-thin" x1="1640" y1="1358" x2="1640" y2="1512"/>
    <text class="sans" font-size="12.5"><tspan x="1472" y="1375">Calories</tspan><tspan x="1472" y="1397">Total Fat</tspan><tspan x="1472" y="1419">Sat. Fat</tspan><tspan x="1472" y="1440">Trans Fat</tspan><tspan x="1472" y="1462">Cholest.</tspan><tspan x="1472" y="1484">Sodium</tspan><tspan x="1472" y="1505">Total Carb.</tspan></text>
    <text class="sans" font-size="12.5"><tspan x="1550" y="1375">60</tspan><tspan x="1550" y="1397">0g (0% DV)</tspan><tspan x="1550" y="1419">0g (0% DV)</tspan><tspan x="1550" y="1440">0g</tspan><tspan x="1550" y="1462">0mg (0% DV)</tspan><tspan x="1550" y="1484">0mg (0% DV)</tspan><tspan x="1550" y="1505">17g (6% DV)</tspan></text>
    <text class="sans" font-size="12.5"><tspan x="1654" y="1375">Fiber</tspan><tspan x="1654" y="1397">Total Sugars</tspan><tspan x="1654" y="1419">Protein</tspan><tspan x="1654" y="1440">Vit. D</tspan><tspan x="1654" y="1462">Calcium</tspan><tspan x="1654" y="1484">Iron</tspan><tspan x="1654" y="1505">Potas.</tspan></text>
    <text class="sans" font-size="12.5"><tspan x="1732" y="1375">0g (0% DV)</tspan><tspan x="1732" y="1397">17g (34% DV)</tspan><tspan x="1732" y="1419">0g</tspan><tspan x="1732" y="1440">0g (0% DV)</tspan><tspan x="1732" y="1462">0g (0% DV)</tspan><tspan x="1732" y="1484">0g (0% DV)</tspan><tspan x="1732" y="1505">0g (0% DV)</tspan></text>
    <text class="sans mid" x="1640" y="1534" font-size="12.5">One serving adds 17g of sugar of your diet and</text>
    <text class="sans mid" x="1640" y="1552" font-size="12.5">represents 34% of the Daily Value for Added Sugars.</text>
    <line class="rule-thin" x1="1465" y1="1562" x2="1818" y2="1562"/>
    <line class="rule-thin" x1="1577" y1="1562" x2="1577" y2="1630"/>
    <text class="sans end" font-size="9" font-weight="400"><tspan x="1571" y="1578">“DO NOT FEED HONEY</tspan><tspan x="1571" y="1600">TO INFANTS UNDER</tspan><tspan x="1571" y="1621">ONE YEAR OLD”</tspan></text>
    <text class="sans" font-size="12" font-weight="400"><tspan x="1583" y="1580">Amber Hollow Apiary, 112 Quarry Lane</tspan><tspan x="1583" y="1602">Foxglove Springs, WV 25400</tspan><tspan x="1583" y="1623">www.amberhollowapiary.com</tspan></text>
  </g>
</svg>
</body>
</html>
```